logo for security & safety training, education consultants
Marlow Advisory Nest Pte Ltd
Professional
LTC (RET) LIM BOON KEAT ROBERT MBA
DIRECTOR
47 JALAN TEMBUSIRA SINGAPORE 528806
robert@marlownest-example.com
www.marlownest-example.com
Perhaps some iso logo and same award logo in dummies

```html
<!DOCTYPE html>
<html lang="en">
<head>
<meta charset="utf-8">
<title>Marlow Advisory Nest – Business Card</title>
<link href="https://fonts.googleapis.com/css2?family=Open+Sans:wght@400;600;700;800&display=swap" rel="stylesheet">
<style>
  :root {
    --bg: #d9d9d9;
    --card: #ffffff;
    --ink: #1e2233;
    --brand-blue: #2a1ee6;
    --brand-blue-light: #5a5cf0;
    --rule: #2b2b2b;
    --muted: #444a5a;
    --faint: #c9c6ea;
  }
  * { box-sizing: border-box; margin: 0; padding: 0; }
  html, body { width: 1200px; height: 876px; overflow: hidden; }
  body {
    background: var(--bg);
    font-family: "Open Sans", Arial, sans-serif;
    display: flex;
    align-items: center;
    justify-content: center;
    gap: 60px;
  }
  .card {
    width: 540px;
    height: 310px;
    background: var(--card);
    position: relative;
    box-shadow: 0 6px 18px rgba(0,0,0,0.18);
    overflow: hidden;
  }
  /* Front */
  .brand {
    position: absolute;
    top: 42px; left: 0; right: 0;
    display: flex; align-items: center; justify-content: center; gap: 10px;
  }
  .brand-dot {
    width: 26px; height: 26px; border-radius: 50%;
    background: var(--brand-blue);
  }
  .brand-name {
    font-weight: 800; font-size: 36px; color: var(--ink); letter-spacing: 1px;
  }
  .band-wrap {
    position: absolute; top: 122px; left: 0; right: 0;
    border-top: 2px solid var(--rule);
    border-bottom: 2px solid var(--rule);
    padding: 4px 0;
  }
  .band {
    background: linear-gradient(90deg, var(--brand-blue), var(--brand-blue-light) 50%, var(--brand-blue));
    height: 34px;
    display: flex; align-items: center; justify-content: center;
    color: #fff; font-size: 12.5px; font-weight: 600; letter-spacing: 0.3px;
  }
  .band .role { margin-left: 8px; padding-left: 8px; border-left: 1px solid #fff; font-weight: 400; }
  .contacts {
    position: absolute; top: 200px; left: 24px; right: 24px;
    display: grid; grid-template-columns: auto auto auto;
    justify-content: space-between;
    row-gap: 14px; column-gap: 12px;
    font-size: 8.5px; color: var(--muted);
  }
  .contact { display: flex; align-items: center; gap: 5px; white-space: nowrap; }
  .contact svg { width: 12px; height: 12px; flex: none; }
  /* Back */
  .website {
    position: absolute; left: 34px; top: 104px;
    font-size: 19px; letter-spacing: 3px; color: var(--ink); font-weight: 400;
  }
  .emblem-fade {
    position: absolute; right: 30px; top: 156px;
    display: flex; align-items: center; gap: 10px;
  }
  .emblem-fade .fade-dot { width: 40px; height: 40px; border-radius: 50%; background: var(--faint); }
  .emblem-fade .fade-name { font-size: 44px; font-weight: 800; color: var(--faint); }
</style>
</head>
<body>
  <section class="card card-front">
    <div class="brand">
      <span class="brand-dot"></span>
      <span class="brand-name">MARLOW</span>
    </div>
    <div class="band-wrap">
      <div class="band">LTC (RET) LIM BOON KEAT ROBERT MBA<span class="role">DIRECTOR</span></div>
    </div>
    <div class="contacts">
      <div class="contact">
        <svg viewBox="0 0 12 12"><circle cx="6" cy="6" r="6" fill="#2a1ee6"/><path d="M6 2.6a2.2 2.2 0 0 0-2.2 2.2C3.8 6.6 6 9.4 6 9.4s2.2-2.8 2.2-4.6A2.2 2.2 0 0 0 6 2.6z" fill="#fff"/></svg>
        47 JALAN TEMBUSIRA SINGAPORE 528806
      </div>
      <div class="contact">
        <svg viewBox="0 0 12 12"><circle cx="6" cy="6" r="6" fill="#2a1ee6"/><path d="M4 3l1.2 1.4-.6.8a4 4 0 0 0 2.2 2.2l.8-.6L9 8l-.8 1C5.5 9 3 6.5 3 3.8z" fill="#fff"/></svg>
        +65 6111 2233
      </div>
      <div class="contact">
        <svg viewBox="0 0 12 12"><circle cx="6" cy="6" r="6" fill="#2a1ee6"/><rect x="4" y="2.5" width="4" height="7" rx="0.8" fill="#fff"/></svg>
        +65 9000 1234
      </div>
      <div class="contact">
        <svg viewBox="0 0 12 12"><circle cx="6" cy="6" r="6" fill="#2a1ee6"/><path d="M4 3l1.2 1.4-.6.8a4 4 0 0 0 2.2 2.2l.8-.6L9 8l-.8 1C5.5 9 3 6.5 3 3.8z" fill="#fff"/></svg>
        +65 6100 2040
      </div>
      <div class="contact">
        <svg viewBox="0 0 12 12"><circle cx="6" cy="6" r="6" fill="#2a1ee6"/><rect x="3" y="4" width="6" height="4.2" fill="#fff"/><path d="M3 4l3 2.4L9 4" stroke="#2a1ee6" stroke-width="0.7" fill="none"/></svg>
        robert@marlownest-example.com
      </div>
      <div class="contact">
        <svg viewBox="0 0 12 12"><circle cx="6" cy="6" r="6" fill="#2a1ee6"/><circle cx="6" cy="6" r="3" fill="none" stroke="#fff" stroke-width="0.8"/><path d="M3 6h6M6 3v6" stroke="#fff" stroke-width="0.6"/></svg>
        www.marlownest-example.com
      </div>
    </div>
  </section>

  <section class="card card-back">
    <p class="website">www.marlownest-example.com</p>
    <div class="emblem-fade">
      <span class="fade-dot"></span>
      <span class="fade-name">MARLOW</span>
    </div>
  </section>
</body>
</html>
```